Business Card for Language School (2 locations)

We need a sleek business card for a language school that is looking to update our image to be more professional. We work with students ages Pre-Kindergarten through adults. Our idea is to have an all-black business card with white or silver lettering. On the front will be the name of our school (Bright Maple English Academy), and on the back there will be information for our location, phone number, email, and website (and possibly social media information). We have two school branches, so the address, phone number, and email address will be different for each branch, but all of the other information will stay the same. We'd like each branch to have a different color card edge that is neon. We are also open to suggestions and new ideas!

Some answers to questions we have received:
1. The reason we haven't added a logo is because we are looking to get a new one. We hadn't originally planned to do that at this time, but we are going to look into updating our project to include that as another aspect of it. We had previously planned to just include the school name on the front without a logo at this time.
2. We currently have two branches of our school, and we want our business card design to be uniform for each location. While it might make sense to put the information on one card right now, we plan to have more locations in the future, so we want to plan ahead with a unified design right now.
3. Our school addresses and phone numbers can be found on our website: www.brightmapleenglish.example (at the bottom of the page)!
Updates

Part of this contest is also a new logo design. Our previous design was a train, which we would be open to keeping if it had an updated, sleeker design.

Contact Information for Business Card

Card #1:
Bright Maple English Academy (Qiaolin Branch)
Yuqing W. Rd. Sec. 3, Lane 412, No. 29, 1F
Beitou District, Taipei City 11268
02-2649-3058
qiaolin@brightmapleenglish.example

Card #2:
Bright Maple English Academy (Fenghe Branch)
Fulan Road, No. 318, 1F
Songshan District, Taipei City 10573
02-2761-4402
fenghe@brightmapleenglish.example

Both cards:
Website: www.brightmapleenglish.example
Facebook: www.facebook.com/brightmapleenglish
Instagram: @brightmapleenglish

```html
<!DOCTYPE html>
<html lang="en">
<head>
<meta charset="utf-8">
<title>Bright Maple English Academy – Business Cards</title>
<link rel="stylesheet" href="https://fonts.googleapis.com/css2?family=Open+Sans:wght@300;400;700&display=swap">
<style>
  :root {
    --page: #e9e9e9;
    --card-light: #f2f2f2;
    --card-dark: #2f2e2f;
    --card-dark-top: #444344;
    --ink: #2a2a2a;
    --logo-dark: #2b2a2b;
    --logo-light: #ebebeb;
    --edge-blue: #3bb6e3;
    --edge-pink: #d9548a;
    --white: #ffffff;
  }
  * { box-sizing: border-box; margin: 0; padding: 0; }
  html, body {
    width: 1200px;
    height: 797px;
    overflow: hidden;
    background: var(--page);
    font-family: "Open Sans", sans-serif;
  }
  .card-stack {
    width: 1200px;
    height: 797px;
    display: flex;
    flex-direction: column;
    align-items: center;
    justify-content: center;
    gap: 14px;
  }
  .card {
    position: relative;
    width: 322px;
    height: 184px;
    border: 3px solid var(--edge-blue);
  }
  .card--pink { border-color: var(--edge-pink); }
  .card--back { background: var(--card-light); color: var(--ink); }
  .card--front {
    background: linear-gradient(160deg, var(--card-dark-top), var(--card-dark) 60%);
    color: var(--white);
  }

  /* front */
  .brand {
    position: absolute;
    right: 62px;
    top: 42px;
    text-align: right;
    line-height: 1.05;
  }
  .brand__line-light { font-weight: 300; font-size: 19px; display: block; }
  .brand__line-bold { font-weight: 700; font-size: 19px; display: block; }
  .brand__mark {
    position: absolute;
    right: 16px;
    top: 70px;
    width: 40px;
    height: 40px;
    background: var(--logo-light);
  }

  /* back, shared */
  .info {
    position: absolute;
    font-size: 7px;
    line-height: 1.35;
    white-space: nowrap;
  }
  .mark-dark {
    position: absolute;
    width: 36px;
    height: 36px;
    background: var(--logo-dark);
  }
  .mark-light {
    position: absolute;
    width: 36px;
    height: 36px;
    border: 1px solid var(--ink);
    background: var(--logo-light);
  }

  /* back, side-by-side arrangement (blue) */
  .card--row .address { right: 190px; top: 52px; text-align: right; }
  .card--row .mark-dark { left: 132px; top: 54px; }
  .card--row .contact { left: 174px; top: 56px; text-align: left; }

  /* back, stacked arrangement (pink) */
  .card--stacked .address { right: 82px; top: 40px; text-align: right; }
  .card--stacked .mark-dark { right: 40px; top: 42px; }
  .card--stacked .contact { right: 82px; top: 104px; text-align: right; }
  .card--stacked .mark-light { right: 40px; top: 106px; }
</style>
</head>
<body>
<main class="card-stack">

  <section class="card card--back card--blue card--row" aria-label="Qiaolin Branch card back, blue edge">
    <p class="info address">No. 29, Lane 412, Sec. 3,<br>Yuqing W. Rd., 1F<br>Beitou District,<br>Taipei City,<br>Taiwan 11268</p>
    <div class="mark-dark"></div>
    <p class="info contact">+886 2 2649 3058<br>qiaolin@brightmapleenglish.example<br>brightmapleenglish.example<br>facebook.com/brightmapleenglish</p>
  </section>

  <section class="card card--front card--blue" aria-label="Qiaolin Branch card front, blue edge">
    <h1 class="brand">
      <span class="brand__line-light">Bright Maple</span>
      <span class="brand__line-bold">English Academy</span>
    </h1>
    <div class="brand__mark"></div>
  </section>

  <section class="card card--front card--pink" aria-label="Fenghe Branch card front, pink edge">
    <h2 class="brand">
      <span class="brand__line-light">Bright Maple</span>
      <span class="brand__line-bold">English Academy</span>
    </h2>
    <div class="brand__mark"></div>
  </section>

  <section class="card card--back card--pink card--stacked" aria-label="Fenghe Branch card back, pink edge">
    <p class="info address">No. 318, 1F,<br>Fulan Road,<br>Songshan District,<br>Taipei City,<br>Taiwan 10573</p>
    <div class="mark-dark"></div>
    <p class="info contact">+886 2 2761 4402<br>fenghe@brightmapleenglish.example<br>brightmapleenglish.example<br>facebook.com/brightmapleenglish</p>
    <div class="mark-light"></div>
  </section>

</main>
</body>
</html>
```